BRIGHT COLORFUL + 55 FAMILY HISTORY BROCHURE 11 x 17 bifold

11 x 17 Bifold Flyer I have given you the Layout I just need you to make it Pretty

YOU DO NOT NEED TO FOLLOW MY LAYOUT, You can but dont have too

Target Market(s)

55 year old consumers, who could choose our service of Hereditary Cancer Screening

Industry/Entity Type

Health And Wellness

Requirements
Must have
• Must be appealing to Grand Parents, must make them want to test , show lots of pictures of grand children, YOU DO NOT NEED TO FOLLOW MY LAYOUT , You can but dont have too
Nice to have
• use our colors of our logo , YOU DO NOT NEED TO FOLLOW MY LAYOUT , You can but dont have too
Should not have
• YOU DO NOT NEED TO FOLLOW MY LAYOUT, You can but dont have too

```html
<!DOCTYPE html>
<html lang="en">
<head>
<meta charset="utf-8">
<title>Hereditary Cancer Screening Bifold</title>
<link href="https://fonts.googleapis.com/css2?family=Arimo:wght@400;700&display=swap" rel="stylesheet">
<style>
  :root {
    --navy: #0c1f5c;
    --green: #8dc63f;
    --ink: #2b2b2b;
    --label-red: #b01c1c;
    --paper: #ffffff;
    --backdrop: #e9e6e1;
    --photo-warm-a: #e8d6c4;
    --photo-warm-b: #b9a48f;
  }
  * { margin: 0; padding: 0; box-sizing: border-box; }
  html, body { width: 1200px; height: 1200px; overflow: hidden; background: var(--backdrop); }
  body { font-family: "Arimo", Arial, sans-serif; color: var(--ink); position: relative; }

  .spread {
    position: absolute; left: 15px; top: 222px;
    width: 1300px; height: 840px;
    transform: scale(0.9); transform-origin: 0 0;
    background: var(--paper);
    box-shadow: 0 6px 18px rgba(0,0,0,0.18);
    overflow: hidden;
  }
  .spread-art { position: absolute; inset: 0; }

  .headline {
    position: absolute; right: 670px; top: 344px; width: 560px;
    text-align: right; font-size: 31px; line-height: 37.8px; font-weight: 400;
  }
  .body-copy {
    position: absolute; left: 137px; top: 538px; width: 488px;
    font-size: 15px; line-height: 25.5px; text-align: justify;
  }

  .brand { position: absolute; display: flex; align-items: center; gap: 10px; }
  .brand-dot { width: 62px; height: 62px; border-radius: 50%; background: var(--navy); }
  .brand-name {
    color: var(--navy); font-weight: 700; font-size: 21px; line-height: 20px;
    letter-spacing: 1px; padding-left: 8px; border-left: 2px solid var(--navy);
  }
  .brand-footer { left: 35px; top: 745px; }
  .brand-cover { left: 675px; top: 28px; }

  .contact { position: absolute; font-size: 15px; line-height: 24px; white-space: nowrap; }
  .contact b { color: var(--label-red); font-weight: 700; }
  .contact-phones { left: 273px; top: 743px; }
  .contact-fax { left: 427px; top: 743px; padding-left: 10px; border-left: 1px solid #bbb; }
  .footer-web { position: absolute; left: 276px; top: 795px; font-size: 20px; white-space: nowrap; }

  .cover-title {
    position: absolute; left: 678px; top: 607px;
    font-size: 34px; line-height: 42px; font-weight: 400;
  }
  .cover-tagline { position: absolute; left: 679px; top: 761px; font-size: 20px; white-space: nowrap; }
  .cover-web {
    position: absolute; left: 706px; top: 806px;
    font-size: 12px; letter-spacing: 3px; white-space: nowrap;
  }
</style>
</head>
<body>
<div class="spread">
  <svg class="spread-art" width="1300" height="840" viewBox="0 0 1300 840">
    <defs>
      <linearGradient id="familyTones" x1="0" y1="0" x2="1" y2="1">
        <stop offset="0" stop-color="var(--photo-warm-a)"/>
        <stop offset="1" stop-color="var(--photo-warm-b)"/>
      </linearGradient>
      <linearGradient id="outdoorTones" x1="0" y1="0" x2="1" y2="1">
        <stop offset="0" stop-color="#d9c99a"/>
        <stop offset="1" stop-color="#c9b4a2"/>
      </linearGradient>
    </defs>

    <g role="img" aria-label="Photo of grandparents smiling on a sofa with their two grandchildren">
      <polygon points="0,0 505,0 610,205 0,470" fill="url(#familyTones)"/>
    </g>
    <polygon points="505,0 650,0 650,265" fill="var(--navy)"/>
    <polygon points="0,478 612,214 612,230 0,496" fill="var(--navy)"/>
    <polygon points="0,528 600,240 650,295 650,720 0,720" fill="var(--green)"/>
    <rect x="0" y="718" width="650" height="11" fill="var(--navy)"/>

    <g role="img" aria-label="Photo of grandparents laughing with their grandson and granddaughter at home">
      <polygon points="1045,0 1300,0 1300,415 965,598 780,520 705,440 705,215 750,155" fill="url(#familyTones)" stroke="var(--navy)" stroke-width="7"/>
    </g>
    <polygon points="1300,445 1255,525 1300,590" fill="var(--green)"/>
    <g role="img" aria-label="Photo of a grandfather hugging his young grandson outdoors">
      <polygon points="1100,570 1262,570 1300,620 1300,845 1045,845 995,765 1045,640" fill="url(#outdoorTones)" stroke="var(--navy)" stroke-width="7"/>
    </g>
  </svg>

  <p class="headline">Your decision<br>won’t just affect you.<br>It will also impact Your Family,<br>since your test results may<br>Forecast Their Cancer Risks, too.</p>
  <p class="body-copy">We believe it is important to understand what can and cannot be learned with genetic testing. Genetic mutations can increase risks for certain cancers, but this does not mean cancer will definitely develop. You should be prepared to receive positive or negative results. Most people receive Negative Results meaning no mutations associated with an increased risk for the Hereditary cancers.</p>

  <div class="brand brand-footer">
    <span class="brand-dot"></span>
    <span class="brand-name">KINWELL<br>HEALTH<br>GROUP</span>
  </div>
  <p class="contact contact-phones"><b>P</b> : 000-XXX-0000<br><b>C</b> : 000-XXX-0000</p>
  <p class="contact contact-fax"><b>F</b> : 000-XXX-0000<br><b>E</b> : info@kinwell.com</p>
  <p class="footer-web">www.kinwellscreening.com</p>

  <div class="brand brand-cover">
    <span class="brand-dot"></span>
    <span class="brand-name">KINWELL<br>HEALTH<br>GROUP</span>
  </div>
  <h1 class="cover-title">Hereditary<br>Cancer<br>Screening</h1>
  <p class="cover-tagline">"The Test You Take For Them"</p>
  <p class="cover-web">www.kinwellscreening.com</p>
</div>
</body>
</html>
```